Bus Bench Ad Design Needed

Hi there. We would like to design an eye catching bus bench ad! The information that we would like to have on it is found below:

- Our logo which is attached below. We would this to take up at least half of the bus bench.
- Our phone number in bold, very visible to see. 813-562-0947. White numbers on an eye catching colored background.
- Our web address : www.SplitEase247.example
- A "Ring Gary" phrase in a black circle with yellow bold letters. Want the "Ring Gary" to be somewhat angled. We are thinking that the "Ring Gary" should be directly below the image in our logo.
- Our tag line we want somewhere in here as well which is "Divorce made easy - at a price you'll like!"

```html
<!DOCTYPE html>
<html lang="en">
<head>
<meta charset="utf-8">
<title>SplitEase Bus Bench Ad</title>
<link rel="stylesheet" href="https://fonts.googleapis.com/css2?family=Anton&family=Montserrat:ital,wght@1,700&family=Questrial&family=Roboto+Condensed:wght@700&display=swap">
<style>
  :root {
    --brand-blue: #1382c9;
    --ink: #111111;
    --paper: #ffffff;
    --stage: #161616;
    --badge-yellow: #f2ea1a;
    --rule-grey: #b9b9b9;
  }
  * { margin: 0; padding: 0; box-sizing: border-box; }
  html, body {
    width: 1200px; height: 1200px; overflow: hidden;
    background: var(--stage);
  }
  .bench-ad {
    position: absolute; left: 40px; top: 440px;
    width: 1120px; height: 320px;
    background: var(--paper);
    overflow: hidden;
    box-shadow: 0 6px 18px rgba(0,0,0,.5);
  }
  .brand-square {
    position: absolute; left: 150px; top: 40px;
    width: 104px; height: 104px;
    background: var(--brand-blue);
  }
  .brand-divider {
    position: absolute; left: 304px; top: 48px;
    width: 2px; height: 128px;
    background: var(--rule-grey);
  }
  .brand-name {
    position: absolute; left: 320px; top: 38px;
    font-family: "Questrial", sans-serif;
    font-size: 96px; line-height: 1;
    letter-spacing: 4px;
    color: var(--brand-blue);
    text-transform: uppercase;
  }
  .brand-descriptor {
    position: absolute; left: 322px; top: 134px;
    font-family: "Questrial", sans-serif;
    font-size: 43px; line-height: 1;
    color: var(--ink);
    letter-spacing: .5px;
  }
  .tagline {
    position: absolute; left: 382px; top: 195px;
    font-family: "Montserrat", sans-serif;
    font-style: italic; font-weight: 700;
    font-size: 21px; line-height: 1;
    color: var(--ink);
    white-space: nowrap;
  }
  .tagline-accent { color: var(--brand-blue); }
  .contact-band {
    position: absolute; left: 0; top: 238px;
    width: 1120px; height: 82px;
  }
  .contact-band svg { display: block; }
  .contact-row {
    position: absolute; left: 324px; top: 238px;
    height: 82px;
    display: flex; align-items: center; gap: 36px;
    white-space: nowrap;
  }
  .phone {
    display: flex; align-items: center; gap: 14px;
    font-family: "Roboto Condensed", sans-serif;
    font-weight: 700; font-size: 52px; line-height: 1;
    color: var(--paper);
  }
  .phone-icon { width: 38px; height: 38px; flex: none; }
  .web-address {
    font-family: "Questrial", sans-serif;
    font-size: 26px; line-height: 1;
    color: var(--paper);
    padding-top: 6px;
  }
  .ring-badge {
    position: absolute; left: 93px; top: 176px;
    width: 128px; height: 128px;
    border-radius: 50%;
    background: var(--ink);
    border: 3px solid var(--badge-yellow);
    box-shadow: 0 0 0 2px var(--ink);
    display: flex; flex-direction: column; align-items: center; justify-content: center;
    transform: rotate(-14deg);
    font-family: "Anton", sans-serif;
    color: var(--badge-yellow);
    font-size: 34px; line-height: .95;
    text-transform: uppercase;
  }
</style>
</head>
<body>
  <section class="bench-ad">
    <div class="brand-square"></div>
    <div class="brand-divider"></div>
    <div class="brand-name">SplitEase</div>
    <div class="brand-descriptor">Non-Lawyer Documents Service</div>
    <p class="tagline">DIVORCE MADE EASY <span class="tagline-accent">- AT A PRICE YOU'LL LIKE!</span></p>

    <div class="contact-band">
      <svg width="1120" height="82" viewBox="0 0 1120 82">
        <polygon points="235,0 1120,0 1120,82 150,82" fill="var(--brand-blue)"/>
        <polygon points="235,0 255,0 170,82 150,82" fill="#0d6aa6"/>
      </svg>
    </div>

    <div class="contact-row">
      <div class="phone">
        <svg class="phone-icon" viewBox="0 0 40 40" aria-hidden="true">
          <path d="M9 4c2-1 4 0 5 2l3 6c1 2 0 3-1 4l-2 2c2 4 5 7 9 9l2-2c1-1 2-2 4-1l6 3c2 1 3 3 2 5l-2 4c-1 2-3 3-6 2C17 34 6 23 2 11c-1-3 0-5 2-6z" fill="var(--paper)"/>
          <path d="M24 4a12 12 0 0 1 12 12M24 10a6 6 0 0 1 6 6" stroke="var(--paper)" stroke-width="2.5" fill="none" stroke-linecap="round"/>
        </svg>
        <span>813-562-0947</span>
      </div>
      <div class="web-address">www.SplitEase247.example</div>
    </div>

    <div class="ring-badge"><span>Ring</span><span>Gary</span></div>
  </section>
</body>
</html>
```